Fantasy Sports Website Needs Web Design

We are modeling our site functionality from www.korvinpicks.com using the same backend systems, and our site will be Brisomaduel.com with the logo branding attached.
The site should have the following pages: home page, signup pages, games/lobby, rules, live scoring, support/FAQs, contact us.
There should be navication in the footer of the page that includes the different pages along with the Privacy Policy and Terms of Use.

•	80% Male
•	89.8% Caucasian
•	51.5% Not Married
•	Average Age: 34
•	College Degree or More: 78.1%
•	51.6% play video games
•	19% play online poker
•	Stats fairly in line with young male demographic
2 page

```html
<!DOCTYPE html>
<html lang="en">
<head>
<meta charset="utf-8">
<title>Brisomaduel – One Day Fantasy Sports Leagues</title>
<link href="https://fonts.googleapis.com/css2?family=Roboto:wght@300;400;500;700&family=Roboto+Condensed:ital,wght@1,700&display=swap" rel="stylesheet">
<style>
:root{
  --bg-dark:#1b1b1c;
  --bg-section:#232324;
  --bg-band:#202021;
  --bg-footer:#171718;
  --blue:#3a9ad9;
  --red:#e02a2e;
  --text:#c9c9c9;
  --text-dim:#555;
  --white:#fff;
  --line:#333;
}
*{box-sizing:border-box;margin:0;padding:0}
html,body{width:975px;height:1200px;overflow:hidden;background:var(--bg-dark);font-family:'Roboto',sans-serif;color:var(--text)}
.page{position:relative;width:975px;height:1200px}
.hero{position:absolute;left:0;top:0;width:975px;height:451px;
  background:radial-gradient(ellipse at 50% 45%,#8a6a55 0%,#5a3c34 30%,#2f2a2c 65%,#1a1a1c 100%)}
.hero-photo{position:absolute;inset:0;background:linear-gradient(90deg,rgba(170,40,40,.35),rgba(0,0,0,0) 30%,rgba(0,0,0,0) 70%,rgba(170,40,40,.35))}
.header{position:absolute;left:0;top:0;width:975px;height:108px;background:rgba(15,15,16,.82);border-bottom:1px solid #444}
.brand{position:absolute;left:62px;top:40px;display:flex;align-items:center;gap:8px;font-weight:700;font-size:19px;color:var(--white);letter-spacing:.5px}
.brand-mark{width:14px;height:14px;border-radius:50%;background:var(--red)}
.nav{position:absolute;top:50px;left:0;font-size:11px;font-weight:500;color:var(--white);letter-spacing:.6px}
.nav a{color:inherit;text-decoration:none;position:absolute;white-space:nowrap}
.account-box{position:absolute;left:791px;top:33px;width:123px;height:46px;border:2px solid #8a8a8a;display:flex;align-items:center;justify-content:center;font-size:11px;font-weight:500;letter-spacing:.5px}
.account-box .signup{color:var(--blue)}
.account-box .login{color:var(--red)}
.hero-title{position:absolute;left:0;width:975px;top:220px;text-align:center;font-family:'Roboto Condensed',sans-serif;font-style:italic;font-weight:700;font-size:31px;line-height:37px;color:var(--white);text-shadow:0 0 3px #000,0 2px 4px #000;letter-spacing:.5px}
.promo-bar{position:absolute;left:296px;top:299px;width:384px;height:25px;background:rgba(40,40,40,.8);color:var(--blue);font-size:13px;font-weight:500;display:flex;align-items:center;justify-content:center;letter-spacing:.4px}
.btn{position:absolute;background:var(--red);color:var(--white);font-size:11px;font-weight:500;display:flex;align-items:center;justify-content:center;letter-spacing:.4px}
.dots{position:absolute;top:427px;left:459px;display:flex;gap:6px}
.dots span{width:10px;height:10px;border-radius:50%;background:var(--white)}
.dots span:first-child{background:var(--blue)}
.welcome{position:absolute;top:451px;left:0;width:975px;height:187px;background:var(--bg-dark)}
.section-title{color:var(--blue);font-size:18px;font-weight:400;letter-spacing:.5px;position:absolute;white-space:nowrap}
.welcome p{position:absolute;left:62px;top:60px;width:851px;text-align:center;font-size:10.5px;font-weight:300;line-height:19px}
.features{position:absolute;top:638px;left:0;width:975px;height:246px;background:var(--bg-section)}
.video{position:absolute;left:61px;top:65px;width:268px;height:152px;background:#000;border:3px solid #333}
.video-frame{position:absolute;left:0;top:0;width:262px;height:136px;background:radial-gradient(circle at 62% 45%,#4a3a32 0%,#1c1716 45%,#000 80%)}
.video-brand{position:absolute;left:24px;top:38px;color:var(--white);font-size:12px;font-weight:700}
.play{position:absolute;left:116px;top:46px}
.video-bar{position:absolute;left:0;bottom:0;width:262px;height:10px;background:#111;border-top:2px solid var(--red)}
.feature{position:absolute;top:65px;width:160px;text-align:center}
.feature .icon{width:50px;height:50px;margin:0 auto;border-radius:50%;background:var(--red);border:3px solid #3a3a3a;display:flex;align-items:center;justify-content:center}
.feature h3{margin-top:23px;color:var(--red);font-size:11.5px;font-weight:400;line-height:17px;letter-spacing:.3px}
.feature p{margin:2px auto 0;width:150px;font-size:10.5px;font-weight:300;line-height:15px}
.info{position:absolute;top:884px;left:0;width:975px;height:148px;background:var(--bg-band)}
.divider{position:absolute;top:24px;width:1px;height:100px;background:var(--line)}
.arrows{position:absolute;top:24px;color:#aaa;font-size:16px;letter-spacing:10px}
.news-date{position:absolute;left:61px;top:57px;color:var(--red);font-size:11px}
.news-text{position:absolute;left:61px;top:74px;width:235px;font-size:10.5px;font-weight:300;line-height:15px}
.partner{position:absolute;top:63px;width:124px;height:62px;background:#000;border:1px solid #444;display:flex;align-items:center;justify-content:center;text-align:center;color:var(--white);font-size:11px;font-weight:500;line-height:14px}
.podcast-label{position:absolute;left:662px;top:49px;display:flex;align-items:center;gap:8px;color:var(--white);font-size:10px}
.wave{position:absolute;left:662px;top:69px;width:253px;height:53px}
.connect{position:absolute;top:1032px;left:0;width:975px;height:110px;background:var(--bg-section)}
.social{position:absolute;top:40px;width:42px;height:42px;border-radius:50%;background:#2a2a2a;border:3px solid #dcdcdc;color:var(--white);font-size:8.5px;font-weight:500;display:flex;align-items:center;justify-content:center}
.pay{position:absolute;top:45px;width:41px;height:27px;background:#f1f1f1;border-radius:2px;color:#333;font-size:8.5px;font-weight:500;display:flex;align-items:center;justify-content:center}
.footer{position:absolute;top:1142px;left:0;width:975px;height:58px;background:var(--bg-footer);text-align:center;font-size:9.5px;color:var(--text-dim);line-height:58px;letter-spacing:.3px}
.footer b{color:#888;font-weight:400}
</style>
</head>
<body>
<div class="page">
  <section class="hero">
    <div class="hero-photo" role="img" aria-label="Action photo collage of baseball, football, hockey and basketball players in red uniforms in a stadium"></div>
    <h1 class="hero-title">ONE DAY BRISOMADUEL<br>SPORTS LEAGUES</h1>
    <div class="promo-bar">100% DEPOSIT BONUS UP TO $250! USE PROMO CODE</div>
    <div class="btn" style="left:421px;top:337px;width:134px;height:30px">ENTER GAME LOBBY</div>
    <div class="dots"><span></span><span></span><span></span><span></span></div>
  </section>

  <header class="header">
    <div class="brand"><span class="brand-mark"></span>Brisomaduel</div>
    <nav class="nav">
      <a style="left:288px">HOME</a>
      <a style="left:356px">LOBBY</a>
      <a style="left:427px">MY CONTENTS PROMOTIONS</a>
      <a style="left:612px">MY ACCOUNT</a>
      <a style="left:718px">HELP/FAQ</a>
    </nav>
    <div class="account-box"><span class="signup">SIGN UP /&nbsp;</span><span class="login">LOG IN</span></div>
  </header>

  <section class="welcome">
    <h2 class="section-title" style="left:0;width:975px;text-align:center;top:27px">WELCOME TO OUR WEBSITE</h2>
    <p>Aliquam molestie, mi et imperdiet euismod, dui purus auctor tellus, et interdum lacus lectus et ante. Sed accumsan sollicitudin sapien, sit amet adipiscing turpis gravida ac. In congue, neque ac lobortis volutpat, libero mauris varius mi, vitae suscipit ipsum ligula vitae risus. Duis aliquam nibh a dui iaculis viverra id a velit. Vivamus egestas risus in magna varius commodo. Sed semper viverra egestas. Etiam pretium porttitor lectus, vel ornare neque porta volutpat.</p>
    <div class="btn" style="left:439px;top:132px;width:98px;height:30px">READ MORE</div>
  </section>

  <section class="features">
    <h2 class="section-title" style="left:134px;top:27px">WATCH VIDEO</h2>
    <h2 class="section-title" style="left:555px;top:27px">WHY CHOOSE US?</h2>
    <div class="video">
      <div class="video-frame" role="img" aria-label="Video still of a presenter against a dark background"></div>
      <div class="video-brand">Brisomaduel</div>
      <svg class="play" width="36" height="36" viewBox="0 0 36 36"><circle cx="18" cy="18" r="16" fill="rgba(0,0,0,.4)" stroke="#fff" stroke-width="2"/><path d="M14 10 L26 18 L14 26 Z" fill="#fff"/></svg>
      <div class="video-bar"></div>
    </div>
    <div class="feature" style="left:360px">
      <div class="icon"><svg width="22" height="22" viewBox="0 0 24 24" fill="#fff"><path d="M2 10h4v12H2zM8 22h10a2 2 0 0 0 2-1.6l1.5-8A2 2 0 0 0 19.5 10H14l1-5a2 2 0 0 0-3.6-1.4L8 9z"/></svg></div>
      <h3>THE CHALLENGE</h3>
      <p>Aliquam molestie, mi et imperdiet euismod, dui purus auctor tellus, et interdum lacus lectus et ante.</p>
    </div>
    <div class="feature" style="left:557px">
      <div class="icon"><svg width="22" height="22" viewBox="0 0 24 24" fill="#fff"><path d="M6 2h12v6a6 6 0 0 1-12 0zM3 3h3v2H5a2 2 0 0 0 1 3v2a4 4 0 0 1-3-4zM21 3h-3v2h1a2 2 0 0 1-1 3v2a4 4 0 0 0 3-4zM11 14h2v4h3v3H8v-3h3z"/></svg></div>
      <h3>REWARDS</h3>
      <p>Aliquam molestie, mi et imperdiet euismod, dui purus auctor tellus, et interdum lacus lectus et ante.</p>
    </div>
    <div class="feature" style="left:752px">
      <div class="icon"><svg width="22" height="22" viewBox="0 0 24 24" fill="none" stroke="#fff" stroke-width="2"><rect x="3" y="5" width="16" height="15" rx="1"/><path d="M3 10h16M8 3v4M14 3v4"/><circle cx="18" cy="18" r="4" fill="#e02a2e"/></svg></div>
      <h3>THERE'S ALWAYS NEXT DAY<br>OR WEEK</h3>
      <p>Aliquam molestie, mi et imperdiet euismod, dui purus auctor tellus.</p>
    </div>
  </section>

  <section class="info">
    <h2 class="section-title" style="left:60px;top:20px">NEWS</h2>
    <div class="arrows" style="left:256px">‹ ›</div>
    <div class="news-date">APR, 06, 2015</div>
    <p class="news-text">Aliquam molestie, mi et imperdiet euismod, dui purus auctor tellus, et interdum lacus lectus et ante.</p>
    <div class="divider" style="left:330px"></div>
    <h2 class="section-title" style="left:353px;top:20px">PARTNERS</h2>
    <div class="arrows" style="left:581px">‹ ›</div>
    <div class="partner" style="left:353px">Marlow Picks</div>
    <div class="partner" style="left:488px">Harbor Bay<br>Fantasy Sports</div>
    <div class="divider" style="left:633px"></div>
    <h2 class="section-title" style="left:662px;top:20px">PODCAST</h2>
    <div class="podcast-label"><svg width="13" height="13" viewBox="0 0 14 14"><circle cx="7" cy="7" r="6" fill="none" stroke="#e02a2e" stroke-width="1.5"/><path d="M5 4l5 3-5 3z" fill="#e02a2e"/></svg>Brisomaduel</div>
    <svg class="wave" viewBox="0 0 253 53" role="img" aria-label="Podcast audio waveform">
      <defs><pattern id="w" width="3" height="41" patternUnits="userSpaceOnUse"><rect x="0" y="4" width="2" height="33" fill="#3a3a3a"/></pattern></defs>
      <rect width="253" height="53" fill="#f2f2f2"/>
      <rect x="6" y="6" width="240" height="41" fill="url(#w)"/>
      <rect x="224" y="27" width="24" height="12" fill="#222"/>
      <text x="236" y="36" font-size="8" fill="#fff" text-anchor="middle" font-family="Roboto,sans-serif">23:50</text>
    </svg>
  </section>

  <section class="connect">
    <h2 class="section-title" style="left:60px;top:44px">CONNECT US</h2>
    <div class="social" style="left:189px">Orbit</div>
    <div class="social" style="left:240px">Pulse</div>
    <div class="social" style="left:291px">Feed</div>
    <div class="social" style="left:342px">Reelo</div>
    <div class="social" style="left:396px;border-color:#e8632a">Sonar</div>
    <div class="divider" style="left:483px;top:16px;height:80px"></div>
    <h2 class="section-title" style="left:502px;top:49px">SECURE PAYMENT</h2>
    <div class="pay" style="left:677px">Nuvo</div>
    <div class="pay" style="left:727px">Keyra</div>
    <div class="pay" style="left:776px">Ostra</div>
    <div class="pay" style="left:825px">Lumen</div>
    <div class="pay" style="left:873px">Tillo</div>
  </section>

  <footer class="footer">COPYRIGHT ©2015 <b>COMPANYNAME</b> ALL RIGHT RESERVED</footer>
</div>
</body>
</html>
```